Creative Stationary for Solo Law Firm

I am looking for stationary designs for my solo law firm called TM Halvorsen Law PLLC. My logo is attached. I'd like the logo incorporated into the design.

I'm looking for a stationary design that is a bit outside of the box and not too standard or boring. The final design should communicate professionalism.

Target Market(s)

United States Clients, Opposing Counsel

Industry/Entity Type

Legal

Font styles to use
Sans Serif

Requirements
Must have
• The stationary design must incorporate my logo design attached. The design itself must be creative. The envelope design must follow standard United States designs with room for the postage stamp at the top right corner and space for the recipient's address in the middle.

```html
<!DOCTYPE html>
<html lang="en">
<head>
<meta charset="utf-8">
<title>TM Halvorsen Law PLLC — Stationery Set</title>
<link rel="stylesheet" href="https://fonts.googleapis.com/css2?family=Roboto:wght@400;500&family=Quicksand:wght@400;500&display=swap">
<style>
  :root {
    --navy: #212a63;
    --silver: #d9d9dc;
    --band-gray: #d3d3d3;
    --stage: #e4e4e6;
    --paper: #ffffff;
    --ink: #1d1d1f;
    --muted: #c9c9cc;
  }
  * { box-sizing: border-box; margin: 0; padding: 0; }
  html, body { width: 1189px; height: 1200px; overflow: hidden; }
  body { background: var(--stage); position: relative; font-family: "Roboto", Arial, sans-serif; color: var(--ink); }

  .piece { position: absolute; overflow: hidden; }
  .paper { background: var(--paper); box-shadow: 0 1px 2px rgba(0,0,0,.08); }
  .navy-stock { background: var(--navy); }

  .brand-name {
    font-family: "Roboto", Arial, sans-serif;
    font-weight: 400;
    color: var(--navy);
    white-space: nowrap;
    letter-spacing: 0;
  }
  .brand-name--light { color: var(--silver); }

  /* Letterhead */
  .letterhead { left: 50px; top: 110px; width: 508px; height: 657px; }
  .letterhead .brand-name { position: absolute; left: 55px; top: 81px; font-size: 21px; }
  .contact-block {
    position: absolute; right: 49px; top: 63px; text-align: right;
    font-family: "Quicksand", Arial, sans-serif; font-size: 8.3px; line-height: 10.5px; color: var(--navy);
  }
  .contact-block .gap { height: 6px; }
  .contact-line { display: flex; justify-content: flex-end; align-items: center; gap: 4px; }
  .contact-line .ico { width: 6px; height: 6px; background: var(--muted); display: inline-block; }
  .recipient { position: absolute; left: 55px; top: 186px; font-size: 8.6px; line-height: 10.5px; }
  .recipient strong { font-weight: 500; font-size: 9.8px; display: block; margin-bottom: 4px; }
  .letter-body { position: absolute; left: 55px; top: 253px; width: 392px; font-size: 9.1px; line-height: 15px; }
  .letter-body p + p { margin-top: 14.5px; }
  .sign-off { position: absolute; left: 55px; top: 512px; font-size: 9.2px; }
  .signature-area { position: absolute; left: 55px; top: 534px; width: 118px; height: 38px; background: linear-gradient(90deg, #ececee, #f6f6f7); }
  .signer { position: absolute; left: 55px; top: 576px; font-size: 9.4px; line-height: 12px; }
  .signer strong { font-weight: 500; font-size: 10px; display: block; }
  .foot-band { position: absolute; left: 0; bottom: 0; }

  /* Folder */
  .folder { left: 629px; top: 111px; width: 506px; height: 654px; }
  .folder-spine { position: absolute; left: 20px; top: 6px; width: 2px; height: 642px; background: rgba(0,0,0,.22); }
  .folder .brand-name { position: absolute; left: 0; right: 0; top: 154px; text-align: center; font-size: 27px; }
  .folder-url { position: absolute; left: 0; right: 0; top: 600px; text-align: center; font-family: "Quicksand", Arial, sans-serif; font-size: 8.5px; color: var(--silver); }

  /* Envelope front */
  .envelope-front { left: 47px; top: 849px; width: 401px; height: 201px; }
  .envelope-front .brand-name { position: absolute; left: 17px; top: 36px; font-size: 15px; }
  .stamp-box { position: absolute; left: 339px; top: 26px; width: 36px; height: 39px; border: 1px solid var(--navy); }
  .address-window { position: absolute; left: 166px; top: 98px; width: 151px; height: 63px; border: 1px solid var(--navy); padding: 10px 9px; color: var(--navy); font-family: "Quicksand", Arial, sans-serif; font-size: 5.8px; line-height: 7.5px; }
  .address-window strong { font-family: "Roboto", Arial, sans-serif; font-weight: 400; font-size: 8px; display: block; margin-bottom: 6px; }

  /* Envelope back */
  .envelope-back { left: 479px; top: 849px; width: 401px; height: 201px; }
  .envelope-flap { position: absolute; left: 0; top: 0; }
  .envelope-back .brand-name { position: absolute; left: 0; right: 0; top: 23px; text-align: center; font-size: 13px; }

  /* Business card */
  .card-back { left: 921px; top: 805px; width: 214px; height: 122px; }
  .card-back .brand-name { position: absolute; left: 0; right: 0; top: 54px; text-align: center; font-size: 12px; }
  .card-front { left: 921px; top: 953px; width: 215px; height: 123px; }
  .card-front .brand-name { position: absolute; left: 11px; top: 30px; font-size: 12px; }
  .card-person { position: absolute; right: 10px; top: 66px; text-align: right; }
  .card-person strong { font-family: "Roboto", Arial, sans-serif; font-weight: 500; font-size: 8.5px; color: var(--navy); display: block; line-height: 9px; }
  .card-person span { font-size: 5px; color: var(--muted); display: block; }
  .card-rule { position: absolute; left: 11px; right: 10px; top: 79px; height: 1px; background: #e2e2e4; }
  .card-contacts { position: absolute; left: 11px; top: 89px; font-family: "Quicksand", Arial, sans-serif; font-size: 5.6px; line-height: 7.3px; color: var(--navy); }
  .card-contacts div { display: flex; align-items: center; gap: 3px; }
  .card-contacts .ico { width: 5px; height: 5px; border: .6px solid var(--muted); display: inline-block; }
  .card-address { position: absolute; right: 10px; top: 97px; text-align: right; font-family: "Quicksand", Arial, sans-serif; font-size: 5.6px; line-height: 7.3px; color: var(--navy); }
</style>
</head>
<body>

<section class="piece paper letterhead">
  <div class="brand-name">TM Halvorsen Law PLLC</div>
  <div class="contact-block">
    <div>0000 Youe Address,2nd Ste.</div>
    <div>Larkfield, Texas 1234</div>
    <div class="gap"></div>
    <div class="contact-line">123 456 7890 <i class="ico"></i></div>
    <div class="contact-line">your@yourcompany.com <i class="ico"></i></div>
    <div class="contact-line">www.yourcompany.com <i class="ico"></i></div>
  </div>
  <div class="recipient">
    <strong>JOHN SMITH</strong>
    Street Name,City Name.<br>Zip Coad 0000
  </div>
  <div class="letter-body">
    <p>Lorem Ipsum is simply dummy text of the printing and typesetting industry. Lorem Ipsum has been the industry's standard dummy text ever since the 1500s, when an unknown printer took a galley of type and scrambled it to make a type specimen book. It has survived not only five centuries, but also the leap into electronic typesetting, remaining essentially unchanged. It was popularised in the 1960s with the release of Letraset sheets containing Lorem Ipsum passages, and more recently with desktop publishing software like Aldus PageMaker including versions of Lorem Ipsum.</p>
    <p>It is a long established fact that a reader will be distracted by the readable content of a page when looking at its layout. The point of using Lorem Ipsum is that it has a more-or-less normal distribution of letters, as opposed to using 'Content here, content here', making it look like readable English. Many desktop publishing packages and web page editors now use Lorem Ipsum as their default model text, and a search for 'lorem ipsum' will uncover many web sites still in their infancy. Various versions have evolved over the years, sometimes by accident, sometimes on purpose (injected humour and the like).</p>
  </div>
  <div class="sign-off">Regards,</div>
  <div class="signature-area" role="img" aria-label="Handwritten signature"></div>
  <div class="signer"><strong>John Doe</strong>General Maneger</div>
  <svg class="foot-band" width="508" height="22" viewBox="0 0 508 22">
    <polygon points="0,7 317,7 311,22 0,22" fill="var(--band-gray)"/>
    <polygon points="322,0 508,0 508,22 313,22" fill="var(--navy)"/>
  </svg>
</section>

<section class="piece navy-stock folder">
  <div class="folder-spine"></div>
  <div class="brand-name brand-name--light">TM Halvorsen Law PLLC</div>
  <div class="folder-url">www.yourcompany.com</div>
</section>

<section class="piece paper envelope-front">
  <div class="brand-name">TM Halvorsen Law PLLC</div>
  <div class="stamp-box"></div>
  <div class="address-window">
    <strong>JOHN SMITH</strong>
    0000 Youe Address,2nd Ste.<br>Larkfield, Texas 1234<br>12345
  </div>
  <svg class="foot-band" width="401" height="16" viewBox="0 0 401 16">
    <polygon points="0,5 246,5 241,16 0,16" fill="var(--band-gray)"/>
    <polygon points="250,0 401,0 401,16 243,16" fill="var(--navy)"/>
  </svg>
</section>

<section class="piece paper envelope-back">
  <svg class="envelope-flap" width="401" height="58" viewBox="0 0 401 58">
    <path d="M0,0 H401 L394,52 Q393,57 388,57 H13 Q8,57 7,52 Z" fill="var(--navy)"/>
  </svg>
  <div class="brand-name brand-name--light">TM Halvorsen Law PLLC</div>
</section>

<section class="piece navy-stock card-back">
  <div class="brand-name brand-name--light">TM Halvorsen Law PLLC</div>
</section>

<section class="piece paper card-front">
  <div class="brand-name">TM Halvorsen Law PLLC</div>
  <div class="card-person"><strong>Employee Name</strong><span>Principal</span></div>
  <div class="card-rule"></div>
  <div class="card-contacts">
    <div><i class="ico"></i>000 000 0000</div>
    <div><i class="ico"></i>yourcompany@gmail.com</div>
    <div><i class="ico"></i>www.yourcompany.com</div>
  </div>
  <div class="card-address">0000 Youe Address,2nd Ste.<br>Larkfield, Texas 1234</div>
  <svg class="foot-band" width="215" height="7" viewBox="0 0 215 7">
    <polygon points="0,2 132,2 131,7 0,7" fill="var(--band-gray)"/>
    <polygon points="136,0 215,0 215,7 133,7" fill="var(--navy)"/>
  </svg>
</section>

</body>
</html>
```